Business Card Design

​Silver Harbor Grooves provides personal, friendly service in a fun and high energy environment. We are based in Vermont.

We would like a card that appeals to a wide range of audiences as we do a wide range of events. Please feel free to check out our website silverharborgrooves.com for inspiration.

Target Market(s)

weddings, corporate, birthday parties, colleges

Industry/Entity Type

Business

Contact Information for Business Card

Silver Harbor Grooves
Providing Entertainment For All Occasions
555 218 6093
silverharborgrooves@mailvane.com
silverharborgrooves.com

```html
<!DOCTYPE html>
<html lang="en">
<head>
<meta charset="utf-8">
<title>Silver Harbor Grooves — Business Card</title>
<link href="https://fonts.googleapis.com/css2?family=Cinzel:wght@600&family=Questrial&display=swap" rel="stylesheet">
<style>
  :root {
    --backdrop: #1c1c1c;
    --card-black: #050505;
    --card-white: #ffffff;
    --brand-green: #3c6a28;
    --accent-red: #b3262b;
    --text-light: #f2f2f2;
  }
  * { margin: 0; padding: 0; box-sizing: border-box; }
  html, body { width: 1200px; height: 871px; overflow: hidden; }
  body {
    background: var(--backdrop);
    font-family: "Questrial", "Century Gothic", sans-serif;
    display: flex;
    align-items: center;
    justify-content: center;
    gap: 40px;
  }
  .card {
    position: relative;
    width: 540px;
    height: 309px;
    overflow: hidden;
    box-shadow: 0 12px 30px rgba(0,0,0,.5);
  }

  /* Back side */
  .card-back {
    background: var(--card-black);
    display: flex;
    align-items: center;
    justify-content: center;
  }

  /* Brand name in place of the mark */
  .brand {
    display: flex;
    align-items: center;
    gap: 10px;
    color: var(--brand-green);
    font-size: 26px;
    letter-spacing: 1px;
    text-transform: uppercase;
  }
  .brand-dot {
    width: 14px; height: 14px;
    border-radius: 50%;
    background: var(--brand-green);
  }

  /* Front side */
  .card-front { background: var(--card-white); }
  .front-top {
    position: absolute;
    left: 0; top: 0; width: 100%; height: 132px;
    display: flex;
    align-items: flex-end;
    justify-content: center;
    padding-bottom: 14px;
  }
  .front-band {
    position: absolute;
    left: 0; top: 132px; width: 100%; height: 148px;
    background: var(--card-black);
  }
  .holder {
    position: absolute;
    left: 58px; top: 40px;
  }
  .holder-name {
    font-family: "Cinzel", Georgia, serif;
    font-weight: 600;
    color: var(--text-light);
    font-size: 15px;
    letter-spacing: 1px;
  }
  .holder-title {
    color: var(--accent-red);
    font-size: 10px;
    margin: 6px 0 0 64px;
  }
  .contact {
    position: absolute;
    left: 272px; top: 38px;
    list-style: none;
  }
  .contact li {
    display: flex;
    align-items: center;
    gap: 14px;
    color: var(--text-light);
    font-size: 12.5px;
    letter-spacing: .6px;
    height: 22px;
  }
  .contact svg { width: 14px; height: 14px; flex: none; }
</style>
</head>
<body>
  <section class="card card-back" aria-label="Card back">
    <div class="brand"><span class="brand-dot"></span>Silver Harbor Grooves</div>
  </section>

  <section class="card card-front" aria-label="Card front">
    <div class="front-top">
      <div class="brand"><span class="brand-dot"></span>Silver Harbor Grooves</div>
    </div>
    <div class="front-band">
      <div class="holder">
        <p class="holder-name">Mara Ellison</p>
        <p class="holder-title">CEO</p>
      </div>
      <ul class="contact">
        <li>
          <svg viewBox="0 0 16 16" fill="none" stroke="#3c6a28" stroke-width="1.6"><path d="M2 6c0-2 3-3 6-3s6 1 6 3l-2 1-1-2H5L4 7z"/><rect x="4" y="8" width="8" height="5" rx="1"/></svg>
          555 218 6093
        </li>
        <li>
          <svg viewBox="0 0 16 16" fill="none" stroke="#3c6a28" stroke-width="1.6"><rect x="1.5" y="3.5" width="13" height="9"/><path d="M1.5 3.5 8 9l6.5-5.5"/></svg>
          silverharborgrooves@mailvane.com
        </li>
        <li>
          <svg viewBox="0 0 16 16" fill="none" stroke="#3c6a28" stroke-width="1.6"><circle cx="8" cy="8" r="6.5"/><path d="M1.5 8h13M8 1.5c-3 3.5-3 9.5 0 13M8 1.5c3 3.5 3 9.5 0 13"/></svg>
          silverharborgrooves.com
        </li>
      </ul>
    </div>
  </section>
</body>
</html>
```